Corvane Summit 2018 Conference flyer

We require a professionally designed flyer for printing and soft copy distributing. The current flyer attached with the information that is required. We need a modern, eye catching flyer to accompany the banner. The banner should represent what the conference is all about. We require the Corvane Lab colours as featured in the current banner. The information needs to be legible and well spaced out so people can find the information quickly.

Target Market(s)

Relating to healthcare professionals, scientists, engineers

Font styles to use
Sans Serif

```html
<!DOCTYPE html>
<html lang="en">
<head>
<meta charset="utf-8">
<title>Corvane Summit 2018 Conference</title>
<link href="https://fonts.googleapis.com/css2?family=Arimo:wght@400;700&family=Montserrat:wght@400;500;600&family=Oswald:wght@500;600&display=swap" rel="stylesheet">
<style>
  :root {
    --purple: #35287a;
    --navy: #2b2f8c;
    --pink: #e8197a;
    --ink: #1d1d2b;
    --sky: #d9f0f8;
    --grey-bg: #3b3d40;
    --frame: #e3e3e3;
    --green: #1a5d4a;
  }
  * { margin: 0; padding: 0; box-sizing: border-box; }
  html, body { width: 1200px; height: 1200px; overflow: hidden; }
  body { background: var(--grey-bg); position: relative; font-family: "Arimo", Arial, sans-serif; }
  .flyer {
    position: absolute; left: 204px; top: 39px; width: 793px; height: 1122px;
    background: linear-gradient(to bottom, var(--sky) 0, #ffffff 200px, #ffffff 100%);
    overflow: hidden;
  }
  .flyer > * { position: absolute; white-space: nowrap; }
  .title {
    left: 0; right: 0; top: 48px; text-align: center;
    font-size: 62px; font-weight: 700; color: var(--purple); letter-spacing: -0.5px;
  }
  .title .year { color: var(--pink); }
  .hero-frame {
    left: 44px; top: 134px; width: 708px; height: 368px;
    background: #f4f4f4; border: 1px solid var(--frame); padding: 9px;
    box-shadow: 0 1px 4px rgba(0,0,0,0.15);
  }
  .hero {
    width: 100%; height: 100%;
    background:
      radial-gradient(circle at 22% 55%, rgba(230,40,40,0.55), transparent 30%),
      radial-gradient(circle at 85% 60%, rgba(30,50,150,0.55), transparent 28%),
      radial-gradient(circle at 48% 55%, rgba(80,240,60,0.45), transparent 15%),
      linear-gradient(135deg, #ececec, #d8d6d4);
  }
  .icon { width: 50px; height: 50px; }
  .icon-date { left: 46px; top: 523px; }
  .icon-time { left: 385px; top: 523px; }
  .icon-place { left: 46px; top: 596px; }
  .date-days { left: 111px; top: 520px; font-size: 20px; font-weight: 700; color: var(--purple); }
  .date-month { left: 111px; top: 542px; font-family: "Montserrat", sans-serif; font-size: 29px; font-weight: 600; color: var(--pink); letter-spacing: 0.5px; }
  .start-time { left: 450px; top: 538px; font-size: 19px; font-weight: 700; color: var(--purple); }
  .start-time span { color: var(--pink); }
  .venue { left: 113px; top: 600px; font-size: 19px; font-weight: 700; color: var(--ink); line-height: 23.5px; }
  .links { left: 382px; top: 600px; font-family: "Montserrat", sans-serif; font-size: 15px; color: var(--ink); line-height: 34.5px; }
  .links b { color: var(--pink); font-weight: 500; }
  .intro { left: 46px; top: 716px; width: 720px; white-space: normal !important; font-family: "Montserrat", sans-serif; font-weight: 500; font-size: 15px; color: var(--ink); line-height: 20px; }
  .aims { left: 46px; top: 764px; list-style: none; font-family: "Montserrat", sans-serif; font-size: 15.5px; color: #2a2a36; }
  .aims li { height: 29.5px; display: flex; align-items: center; gap: 10px; }
  .aims svg { width: 13px; height: 13px; flex: none; }
  .event-mark { left: 71px; top: 930px; width: 120px; white-space: normal !important; font-size: 25px; font-weight: 700; color: var(--purple); line-height: 30px; }
  .event-mark::before { content: ""; display: block; width: 22px; height: 22px; background: var(--pink); margin-bottom: 10px; }
  .hand-art {
    left: 200px; top: 896px; width: 90px; height: 150px;
    background: linear-gradient(160deg, #4a5fd0, #1c2a8a);
    border-radius: 40% 30% 45% 35%;
  }
  .promo { left: 335px; top: 911px; width: 412px; height: 91px; }
  .promo-label { position: absolute; left: 18px; top: 8px; font-family: "Oswald", sans-serif; font-size: 27px; line-height: 38px; color: #ffffff; font-weight: 500; transform: scaleX(0.85); transform-origin: left; }
  .promo-offer { position: absolute; left: 138px; top: 2px; font-family: "Oswald", sans-serif; font-weight: 600; font-size: 48px; line-height: 62px; color: #ffffff; white-space: nowrap; transform: scaleX(0.9); transform-origin: left; }
  .promo-note { position: absolute; left: 138px; top: 66px; font-family: "Montserrat", sans-serif; font-size: 13px; font-weight: 500; color: #ffffff; white-space: nowrap; }
  .partner { top: 1052px; font-weight: 700; display: flex; align-items: center; gap: 7px; }
  .partner-a { left: 306px; font-size: 22px; color: #222; }
  .partner-b { left: 468px; font-size: 20px; color: var(--green); }
  .partner-c { left: 672px; top: 1044px; font-size: 12px; line-height: 15px; color: var(--navy); text-align: center; white-space: normal !important; width: 80px; display: block; }
  .partner i { width: 14px; height: 14px; background: currentColor; display: block; flex: none; }
  .base-bar { left: 0; bottom: 0; width: 793px; height: 10px; }
</style>
</head>
<body>
  <main class="flyer">
    <h1 class="title">Corvane Summit <span class="year">2018</span></h1>

    <div class="hero-frame">
      <div class="hero" role="img" aria-label="Photograph of colourful 3D printed anatomical models: red arterial tree, white heart, green and blue parts and a blue robotic hand"></div>
    </div>

    <svg class="icon icon-date" viewBox="0 0 50 50" aria-hidden="true">
      <circle cx="25" cy="25" r="23" fill="none" stroke="var(--pink)" stroke-width="2.5"/>
      <circle cx="25" cy="25" r="18" fill="#7a7a84"/>
      <rect x="16" y="17" width="18" height="16" rx="2" fill="none" stroke="#fff" stroke-width="1.8"/>
      <line x1="16" y1="21.5" x2="34" y2="21.5" stroke="#fff" stroke-width="1.8"/>
      <g fill="#fff"><rect x="19" y="24" width="3" height="2.5"/><rect x="23.5" y="24" width="3" height="2.5"/><rect x="28" y="24" width="3" height="2.5"/><rect x="19" y="28" width="3" height="2.5"/><rect x="23.5" y="28" width="3" height="2.5"/></g>
    </svg>
    <p class="date-days">Saturday 13 &amp; Sunday 14</p>
    <p class="date-month">OCTOBER 2018</p>

    <svg class="icon icon-time" viewBox="0 0 50 50" aria-hidden="true">
      <circle cx="25" cy="25" r="23" fill="none" stroke="var(--pink)" stroke-width="2.5"/>
      <circle cx="25" cy="25" r="18" fill="#7a7a84"/>
      <circle cx="25" cy="25" r="10" fill="none" stroke="#fff" stroke-width="1.8"/>
      <path d="M25 18.5V25l4 3" fill="none" stroke="#fff" stroke-width="1.8" stroke-linecap="round"/>
    </svg>
    <p class="start-time">Starting at <span>0900hrs</span></p>

    <svg class="icon icon-place" viewBox="0 0 50 50" aria-hidden="true">
      <circle cx="25" cy="25" r="23" fill="none" stroke="var(--pink)" stroke-width="2.5"/>
      <circle cx="25" cy="25" r="18" fill="#7a7a84"/>
      <path d="M25 35c-5-6-8-10-8-14a8 8 0 0 1 16 0c0 4-3 8-8 14z" fill="none" stroke="#fff" stroke-width="1.8"/>
      <circle cx="25" cy="21" r="3" fill="none" stroke="#fff" stroke-width="1.8"/>
    </svg>
    <p class="venue">Halden Neuro Centre<br>Ashgrove Building<br>88/12 Linden Parade<br>ELMVALE&nbsp; VIC&nbsp; 3999</p>

    <p class="links">
      <b>More info:</b> https://corvanelab.org.au/summit18/<br>
      <b>Registration:</b> https://corvanelab.org.au/registration/<br>
      <b>Enquiries:</b> printlab@norbrookhealth.org
    </p>

    <p class="intro">The @CorvaneLab at Norbrook Health warmly invites you to attend the 2018 Corvane Summit Symposium. This cross-disciplinary event will:</p>

    <ul class="aims">
      <li><svg viewBox="0 0 13 13"><circle cx="6.5" cy="6.5" r="5.5" fill="none" stroke="var(--navy)" stroke-width="1.3"/><path d="M4 6.7l1.8 1.8L9.3 4.8" fill="none" stroke="var(--navy)" stroke-width="1.3"/></svg>Showcase clinical applications of 3d modelling and printing</li>
      <li><svg viewBox="0 0 13 13"><circle cx="6.5" cy="6.5" r="5.5" fill="none" stroke="var(--navy)" stroke-width="1.3"/><path d="M4 6.7l1.8 1.8L9.3 4.8" fill="none" stroke="var(--navy)" stroke-width="1.3"/></svg>Explore the use of Virtual Reality in Medicine</li>
      <li><svg viewBox="0 0 13 13"><circle cx="6.5" cy="6.5" r="5.5" fill="none" stroke="var(--navy)" stroke-width="1.3"/><path d="M4 6.7l1.8 1.8L9.3 4.8" fill="none" stroke="var(--navy)" stroke-width="1.3"/></svg>Bring together clinicians, engineers and thought leaders in medical 3D printing</li>
      <li><svg viewBox="0 0 13 13"><circle cx="6.5" cy="6.5" r="5.5" fill="none" stroke="var(--navy)" stroke-width="1.3"/><path d="M4 6.7l1.8 1.8L9.3 4.8" fill="none" stroke="var(--navy)" stroke-width="1.3"/></svg>Discuss social &amp; legal issues in medical 3d printing</li>
    </ul>

    <p class="event-mark">Corvane Summit 2018</p>
    <div class="hand-art" role="img" aria-label="Illustration of a blue 3D printed robotic hand"></div>

    <div class="promo">
      <svg width="412" height="91" viewBox="0 0 412 91" style="position:absolute;left:0;top:0" aria-hidden="true">
        <polygon points="0,0 128,0 104,91 0,91" fill="var(--navy)"/>
        <polygon points="128,0 412,0 412,91 104,91" fill="var(--pink)"/>
      </svg>
      <p class="promo-label">DISCOUNT<br>CODE:</p>
      <p class="promo-offer">GET 50% OFF</p>
      <p class="promo-note">your ticket if you enter CVPROMO</p>
    </div>

    <p class="partner partner-a">Halvern</p>
    <p class="partner partner-b"><i></i>Norbrook Health</p>
    <p class="partner partner-c">Eastmere University</p>

    <svg class="base-bar" viewBox="0 0 793 10" aria-hidden="true">
      <polygon points="0,0 293,0 288,10 0,10" fill="var(--pink)"/>
      <polygon points="296,0 793,0 793,10 291,10" fill="var(--navy)"/>
    </svg>
  </main>
</body>
</html>
```